KINDLEA: Flu Social Media Post #2

- Please create a similar design to the one attached to create a Social Media Post image.
- Attached, Logo, boarder, sample flu social media image.
- KINDLEA - must be included
- Flu - must be included
- Protect your community. Protect Your Elders. Stay Vaccinated. - must be included
- image of mom/daughter holding hands must be included
- For inspiration, https://brovelink.example/, and https://www.facebook.com/Brovelink

```html
<!DOCTYPE html>
<html lang="en">
<head>
<meta charset="utf-8">
<title>KINDLEA – Flu Social Media Post</title>
<link rel="stylesheet" href="https://fonts.googleapis.com/css2?family=Montserrat:wght@700;800;900&display=swap">
<style>
  :root {
    --crimson: #921f2f;
    --crimson-band: rgba(146, 31, 47, 0.9);
    --teal: #52a9b1;
    --blush: #e3c3c2;
    --blush-light: #f0dcdb;
    --white: #ffffff;
    --border-grey: #b9b3b5;
  }
  * { box-sizing: border-box; margin: 0; padding: 0; }
  html, body {
    width: 1200px;
    height: 1196px;
    overflow: hidden;
    background: var(--white);
  }
  body { font-family: "Montserrat", Arial, sans-serif; }

  .post {
    position: relative;
    width: 1200px;
    height: 1196px;
    overflow: hidden;
  }
  .post__border-pattern {
    position: absolute;
    inset: 0;
    background: linear-gradient(135deg, #c9a3a7 0%, #a9c4c7 50%, #c9a3a7 100%);
  }
  .post__frame {
    position: absolute;
    left: 34px; top: 34px; right: 34px; bottom: 34px;
    background: var(--crimson);
  }
  .post__field {
    position: absolute;
    left: 44px; top: 44px; right: 44px; bottom: 39px;
    background: var(--blush);
    overflow: hidden;
  }

  .title-box {
    position: absolute;
    left: 76px; top: 73px;
    width: 822px; height: 186px;
    border: 9px solid var(--teal);
    display: flex;
    align-items: center;
    justify-content: center;
  }
  .title-box__word {
    color: var(--crimson);
    font-weight: 900;
    font-size: 140px;
    line-height: 1;
    letter-spacing: 6px;
    -webkit-text-stroke: 2px var(--blush-light);
    paint-order: stroke fill;
  }

  .org-mark {
    position: absolute;
    left: 940px; top: 120px;
    width: 180px;
    display: flex;
    flex-direction: column;
    align-items: center;
    gap: 12px;
  }
  .org-mark__dot {
    width: 58px; height: 58px;
    border-radius: 50%;
    background: var(--teal);
  }
  .org-mark__name {
    color: var(--teal);
    font-weight: 800;
    font-size: 19px;
    line-height: 1.15;
    text-align: center;
    text-transform: uppercase;
  }

  .headline {
    position: absolute;
    left: 0; right: 0;
    top: 322px;
    text-align: center;
    font-weight: 800;
    font-size: 72px;
    line-height: 90px;
    -webkit-text-stroke: 6px var(--white);
    paint-order: stroke fill;
  }
  .headline__lead { color: var(--teal); }
  .headline__key { color: var(--crimson); }

  .photo {
    position: absolute;
    left: 70px; top: 508px;
    width: 1067px; height: 649px;
    background:
      radial-gradient(ellipse 22% 30% at 18% 18%, #2a2220 0%, rgba(42,34,32,0) 100%),
      radial-gradient(ellipse 22% 34% at 82% 22%, #1a1514 0%, rgba(26,21,20,0) 100%),
      linear-gradient(90deg, rgba(90,40,80,0.75) 0%, rgba(180,150,160,0.5) 35%, rgba(227,195,194,0) 50%, rgba(120,40,40,0.55) 65%, rgba(30,20,20,0.85) 100%);
  }

  .action-band {
    position: absolute;
    left: 44px; right: 44px;
    top: 798px; height: 122px;
    background: linear-gradient(90deg, rgba(255,255,255,0.35), rgba(255,255,255,0.6) 50%, rgba(255,255,255,0.35));
    display: flex;
    align-items: center;
    justify-content: center;
  }
  .action-band__text {
    color: var(--teal);
    font-weight: 800;
    font-size: 104px;
    line-height: 1;
    margin-left: -70px;
    -webkit-text-stroke: 7px var(--white);
    paint-order: stroke fill;
  }

  .info-bar {
    position: absolute;
    left: 44px; right: 44px;
    top: 1019px; height: 87px;
    background: var(--crimson-band);
    display: flex;
    align-items: center;
    justify-content: center;
  }
  .info-bar__text {
    color: var(--white);
    font-weight: 800;
    font-size: 37px;
    letter-spacing: 0.2px;
  }
</style>
</head>
<body>
  <main class="post">
    <div class="post__border-pattern" role="img" aria-label="Woven zigzag border in rose and teal"></div>
    <div class="post__frame"></div>
    <div class="post__field" role="img" aria-label="Soft blush background with faint woven motifs"></div>

    <div class="title-box">
      <h1 class="title-box__word">KINDLEA</h1>
    </div>

    <div class="org-mark">
      <span class="org-mark__dot"></span>
      <span class="org-mark__name">Brovelink Elder Circle</span>
    </div>

    <div class="photo" role="img" aria-label="Photo from behind of a mother and daughter in embroidered blouses holding hands"></div>

    <h2 class="headline">
      <span class="headline__lead">Protect Your </span><span class="headline__key">Community</span><br>
      <span class="headline__lead">Protect Your </span><span class="headline__key">Elders</span>
    </h2>

    <div class="action-band">
      <p class="action-band__text">Stay Vaccinated</p>
    </div>

    <div class="info-bar">
      <p class="info-bar__text">Learn more about getting vaccinated against the Flu</p>
    </div>
  </main>
</body>
</html>
```